Werbebrief
Zielgruppe
Unsere Zielgruppe sind Geschäftsführer junger Unternehmen.
Hallo,
Wir benötigen einen "Werbebrief". Es ist jedoch weniger ein Brief, als viel mehr eine etwas größerer "Werbekarte" (diese soll 105 x 210mm groß sein).
Auf der Vorderseite soll folgender Text stehen:
Für Unternehmen, die gerne expandieren möchten
Auf der Rückseite soll folgender Link stehen:
www.tolvek-werk.de/Expandieren
Darunter soll folgendes stehen:
Ihr persönlicher Code: ABC123
Wichtig ist, dass wir den Code individuell ändern können, da jeder einen anderen Code bekommt.
Unser Logo und Corporate Farbe habe ich hochgeladen. Das Design sollte auf jeden Fall zu unserer Webseite passen (www.tolvek-werk.de)
Wir freuen uns auf Ihre Vorschläge.

```html
<!DOCTYPE html>
<html lang="de">
<head>
<meta charset="utf-8">
<title>Tolvek Werk – Werbekarte</title>
<link rel="stylesheet" href="https://fonts.googleapis.com/css2?family=Carlito:wght@400&display=swap">
<style>
  :root {
    --page-bg: #e8e5e1;
    --card-blue: #22509a;
    --card-blue-light: #2a5ca6;
    --card-blue-dark: #1d4689;
    --accent-green: #8dc63f;
    --text-white: #ffffff;
    --card-shadow: rgba(0, 0, 0, 0.25);
  }
  * { margin: 0; padding: 0; box-sizing: border-box; }
  html, body {
    width: 1200px;
    height: 1200px;
    overflow: hidden;
    background: var(--page-bg);
  }
  .sheet {
    position: relative;
    width: 1200px;
    height: 1200px;
  }
  .card {
    position: absolute;
    left: 193px;
    width: 814px;
    height: 407px;
    box-shadow: 0 6px 18px var(--card-shadow);
  }
  .card--back  { top: 160px; }
  .card--front { top: 654px; }
  .card svg {
    display: block;
    width: 814px;
    height: 407px;
  }
  .card-text {
    font-family: "Carlito", "Calibri", sans-serif;
    fill: var(--text-white);
  }
  .brand-name  { font-size: 27px; }
  .card-url    { font-size: 21px; }
  .card-code   { font-size: 21px; }
  .card-claim  { font-size: 29px; }
</style>
</head>
<body>
<main class="sheet">

  <!-- Rückseite: Link und persönlicher Code -->
  <section class="card card--back" aria-label="Rückseite der Werbekarte">
    <svg viewBox="0 0 678 339" xmlns="http://www.w3.org/2000/svg">
      <defs>
        <linearGradient id="blue-back" x1="0" y1="0" x2="1" y2="1">
          <stop offset="0" stop-color="var(--card-blue-light)"/>
          <stop offset="0.6" stop-color="var(--card-blue)"/>
          <stop offset="1" stop-color="var(--card-blue-dark)"/>
        </linearGradient>
      </defs>
      <rect class="card-base" width="678" height="339" fill="url(#blue-back)"/>
      <path class="band band--top" d="M0 0 H678 V2 C500 6 200 10 0 32 Z" fill="var(--accent-green)"/>
      <path class="band band--bottom" d="M0 339 H678 V292 C640 318 450 326 0 333 Z" fill="var(--accent-green)"/>

      <g class="brand">
        <rect class="brand-mark" x="448" y="40" width="3" height="24" fill="var(--text-white)"/>
        <text class="card-text brand-name" x="650" y="59" text-anchor="end">Tolvek Werk</text>
      </g>

      <text class="card-text card-url" x="40" y="135">www.tolvek-werk.de/Expandieren</text>
      <text class="card-text card-code" x="606" y="289" text-anchor="end">Ihr persönlicher Code: Tol1612</text>
    </svg>
  </section>

  <!-- Vorderseite: Claim -->
  <section class="card card--front" aria-label="Vorderseite der Werbekarte">
    <svg viewBox="0 0 678 339" xmlns="http://www.w3.org/2000/svg">
      <defs>
        <linearGradient id="blue-front" x1="0" y1="0" x2="1" y2="1">
          <stop offset="0" stop-color="var(--card-blue-light)"/>
          <stop offset="0.6" stop-color="var(--card-blue)"/>
          <stop offset="1" stop-color="var(--card-blue-dark)"/>
        </linearGradient>
      </defs>
      <rect class="card-base" width="678" height="339" fill="url(#blue-front)"/>
      <path class="band band--top" d="M0 0 H678 V2 C500 6 200 10 0 32 Z" fill="var(--accent-green)"/>
      <path class="band band--bottom" d="M0 339 H678 V292 C640 318 450 326 0 333 Z" fill="var(--accent-green)"/>

      <g class="brand">
        <rect class="brand-mark" x="448" y="30" width="3" height="24" fill="var(--text-white)"/>
        <text class="card-text brand-name" x="650" y="49" text-anchor="end">Tolvek Werk</text>
      </g>

      <text class="card-text card-claim" x="105" y="165">Für Unternehmen, die gerne</text>
      <text class="card-text card-claim" x="253" y="207">expandieren möchten</text>
    </svg>
  </section>

</main>
</body>
</html>
```